This will be a design for publicity materials for an event:

DEBATE: That the NRC will harm Asia's growing digital economies

Date: 18 July 2013, 19:00-21:00
Venue: Function Room 6, Level 3, The Lorvane Crest, Kota Kinabalu, Malaysia
RSVP: to tobias@welmarch.example by 11 July 2013, limited free tickets available

- blurb begins -

The Meridian Harbour Compact offers a golden opportunity for Asian nations to reap the rich rewards of global trade - or else it poses a dire threat to their sovereignty that would allow foreign multinational corporations to rewrite national laws for their own benefit. Opinions about the merits of the Meridian Harbour Compact for Asia are polarised, making it difficult for ordinary citizens to separate fact from fiction. So what better topic for a debate, to clear the air and shed some light on this impenetrable and controversial subject?

Shoppers Guildwide, in partnership with Byteline Report East, is hosting a free public 3-on-3 parliamentary-style debate on the proposition "That the NRC will harm Asia's growing digital economies". Drawn from across the region's government, industry and NGO communities, the participants will attempt to convince the audience that the NRC is the best hope for stimulating growth and innovation in Asia's high-tech industries - or that it will hamstring those industries with inappropriate laws pushed by foreign interests. Who wins? The audience will decide.

- blurb ends -

We want to have a design in 4 formats to promote this online, but you can just do one format to respond to the brief, and the others can come after I select a winner. One of the formats should be suitable to be emailed, so you could do it either as a graphic, or else as an HTML page suitable for emailing. The second format should be a 430 x 130 banner. Third should be a 300 x 250 banner. Also one format in about 800x600 or similar that we can use as a presentation slide at the venue.
Updates

Just to clarify, you don't need to include the whole blurb text.  Particularly in the small formats, that would be impossible.  It is mainly included as background for you.

I apologise for not getting back to you with comments and feedback - I had to travel to India and don't have proper Internet access here. I will get back to you as soon as I can. 

Target Market(s)

Business people, NGOs, diplomats

Industry/Entity Type

Industry

Requirements
Must have
• Sponsors' logos are attached.
Nice to have
• In at least the larger formats, we need to have space to show the names of the debaters. But we don't have those names yet, so for now it should say something like "Debating teams announced soon", with the facility to change it later when we do have the names. I had thought about maybe using a stage with a curtain drawn for the "coming soon" variant, and the curtains drawn back to reveal the names for the final variant. But I leave this to you.
Should not have
• Prefer if you don't use stock photos of people.

```html
<!DOCTYPE html>
<html lang="en">
<head>
<meta charset="utf-8">
<title>Debate: That the NRC will harm Asia's growing digital economies</title>
<link rel="stylesheet" href="https://fonts.googleapis.com/css2?family=Arimo:wght@400;700&display=swap">
<style>
  :root {
    --navy: #14295a;
    --ink: #0b0b0b;
    --sky-light: #f4f8fc;
    --sky-mid: #c9d9ec;
    --land: #9fb6d6;
    --strip-dark: #0c0f14;
    --strip-mid: #2a333f;
    --strip-blue: #3c5d84;
    --gold: #e9c05a;
    --white: #ffffff;
    --rule: #1c1c1c;
  }
  * { box-sizing: border-box; margin: 0; padding: 0; }
  html, body { width: 1200px; height: 900px; overflow: hidden; background: var(--white); }
  body { font-family: "Arimo", Arial, sans-serif; }

  .poster {
    position: relative;
    width: 1200px;
    height: 900px;
    overflow: hidden;
    background: linear-gradient(135deg, var(--sky-light) 0%, #e6eef7 55%, #dbe6f2 100%);
  }

  .map-backdrop {
    position: absolute;
    left: 198px; top: 0; right: 0; bottom: 0;
    background:
      radial-gradient(ellipse 40% 32% at 42% 30%, var(--land) 0%, rgba(159,182,214,0.55) 55%, transparent 80%),
      radial-gradient(ellipse 22% 30% at 78% 38%, rgba(159,182,214,0.7) 0%, transparent 75%),
      radial-gradient(ellipse 26% 18% at 62% 82%, rgba(159,182,214,0.75) 0%, transparent 80%),
      radial-gradient(ellipse 30% 40% at 15% 55%, rgba(159,182,214,0.4) 0%, transparent 80%);
  }

  .side-strip {
    position: absolute;
    left: 0; top: 0;
    width: 198px; height: 900px;
    background:
      radial-gradient(ellipse 60% 20% at 85% 40%, rgba(60,93,132,0.8) 0%, transparent 80%),
      linear-gradient(180deg, var(--strip-dark) 0%, var(--strip-mid) 45%, #3d4652 70%, var(--strip-dark) 100%);
  }

  .debate-word {
    position: absolute;
    left: 30px; top: 112px;
    width: 80px;
    display: flex;
    flex-direction: column;
    align-items: center;
    gap: 6px;
    font-weight: 700;
    font-size: 104px;
    line-height: 104px;
    color: #1a1d22;
    -webkit-text-stroke: 2px var(--gold);
    text-shadow: 0 0 6px rgba(233,192,90,0.9), 0 0 14px rgba(233,192,90,0.5);
  }

  .motion-lead {
    position: absolute;
    left: 266px; top: 70px;
    font-size: 37px; font-weight: 700;
    color: var(--ink);
    text-shadow: 0 0 3px var(--white), 0 0 3px var(--white);
  }

  .motion {
    position: absolute;
    left: 252px; top: 130px;
    font-weight: 700;
    color: var(--navy);
    line-height: 1;
    -webkit-text-stroke: 2px var(--white);
    paint-order: stroke fill;
    text-shadow: 0 0 4px var(--white), 0 0 4px var(--white);
  }
  .motion-line { display: block; white-space: nowrap; }
  .motion-subject {
    font-size: 66px; color: var(--white);
    -webkit-text-stroke: 3px var(--navy);
    text-shadow: 0 0 3px var(--white);
  }
  .motion-verb { font-size: 32px; vertical-align: 18px; margin-left: 6px; }
  .motion-asia { font-size: 96px; margin-top: -4px; }
  .motion-growing { font-size: 76px; margin-top: 14px; }
  .motion-economies { font-size: 80px; margin-top: 10px; }

  .event-time {
    position: absolute;
    left: 853px; top: 42px;
    font-size: 40px; line-height: 52px;
    color: var(--navy);
  }

  .sponsors {
    position: absolute;
    left: 1080px; top: 266px;
    width: 100px;
    list-style: none;
  }
  .sponsor {
    display: flex;
    align-items: center;
    gap: 6px;
    width: 100px; height: 68px;
    padding: 6px;
    background: var(--white);
    font-size: 12px; font-weight: 700; line-height: 1.15;
    color: var(--navy);
    margin-bottom: 34px;
  }
  .sponsor-dot { flex: none; width: 12px; height: 12px; border-radius: 50%; background: var(--navy); }

  .blurb {
    position: absolute;
    left: 262px; top: 590px;
    width: 900px;
    font-size: 22px; line-height: 30px;
    color: var(--ink);
  }

  .divider {
    position: absolute;
    left: 248px; top: 780px;
    width: 940px; height: 6px;
    border-top: 2px solid var(--rule);
    border-bottom: 1px solid var(--rule);
  }

  .logistics {
    position: absolute;
    left: 250px; top: 805px;
    font-size: 20px; line-height: 30px;
    color: var(--ink);
  }
</style>
</head>
<body>
<main class="poster">
  <div class="map-backdrop" role="img" aria-label="Map of Asia and the Pacific region in soft blue tones"></div>

  <aside class="side-strip" role="img" aria-label="Close-up of a studio microphone on a dark background"></aside>
  <div class="debate-word" aria-label="Debate">
    <span>D</span><span>E</span><span>B</span><span>A</span><span>T</span><span>E</span>
  </div>

  <p class="motion-lead">That the</p>
  <h1 class="motion">
    <span class="motion-line"><span class="motion-subject">NRC</span><span class="motion-verb">will harm</span></span>
    <span class="motion-line motion-asia">Asia's</span>
    <span class="motion-line motion-growing">growing digital</span>
    <span class="motion-line motion-economies">economies</span>
  </h1>

  <p class="event-time">18 July 2013,<br>19:00-21:00</p>

  <ul class="sponsors">
    <li class="sponsor"><span class="sponsor-dot"></span>Even Terms</li>
    <li class="sponsor"><span class="sponsor-dot"></span>Byteline Report East</li>
    <li class="sponsor"><span class="sponsor-dot"></span>Shoppers Guildwide</li>
  </ul>

  <p class="blurb">The Meridian Harbour Compact offers a golden opportunity for Asian nations to reap the rich rewards of global trade or else it poses a dire threat to their sovereignty that would allow foreign multinational corporations to rewrite national laws for their own benefit.</p>

  <div class="divider"></div>

  <p class="logistics">Venue: Function Room 6, Level 3, The Lorvane Crest, Kota Kinabalu, Malaysia<br>RSVP: to tobias@welmarch.example by 11 July 2013, limited free tickets available</p>
</main>
</body>
</html>
```